Buch-/eBook-Cover Budgetplanung
Zielgruppe
Ich bin Autorin und verkaufe unter meiner Marke SparLaterne Bücher und handgemachte Produkte rund um Budgetplanung und bewussten Umgang mit Geld. Meine Zielgruppe sind Frauen ab 45, die ihre Finanzen ordnen und bewusster leben möchten. Sie mögen eine ruhige, hochwertige, leicht nostalgische Ästhetik und werden von lauten, grellen Designs abgeschreckt.
Aufgabenstellung
Buchcover 'Der leere Korb' (VRL), Auftakt einer Cover-Serie
Das Buch:
Ratgeber über bewussten Konsumverzicht: ein Jahr Kaufpause mit monatlichen Challenges. Warm und ermutigend, kein Verbotsbuch. Zielgruppe: Frauen ab 45, die eine ruhige, hochwertige, leicht nostalgische Ästhetik mögen.
Texte auf dem Cover:
Titel: Der leere Korb
Untertitel: Die No-Buy-Challenge: Ein Jahr bewusst nicht kaufen, Geld sparen und herausfinden, was du wirklich brauchst
Autorin: Helene Morwitz
Serie:
Weitere Geld-Ratgeber von mir erhalten danach Cover im selben Stil. Gesucht ist also ein wiederholbares Layout, bei dem sich pro Buch nur Titel und Motiv ändern. Der Gewinner erhält die Folgecover als Direktaufträge.
Stil (Referenzbilder anbei, bitte verbindlich umsetzen):
Marke SparLaterne: Graublau (#95a9af) und Creme, Gold nur als Akzent. Vertikale Streifen als Markenmuster, weiße Spitzenborte, schwarze handgezeichnete Schleife (PNG liegt bei). Schriften: Cormorant Garamond für Versalien, Sloop Pro, Kalligrafieschrift für Akzente. Wirkung: elegantes, feminines Vintage. Das Buchinnere ist bereits in diesem Stil gestaltet (Beispielseiten anbei), das Cover soll dazu passen.
Bitte nicht: Geldscheine, Münzen, Sparschweine, Einkaufstüten, rote Verbotssymbole, grelle Farben, Rosa, überfüllte Layouts.
Wichtigstes Kriterium:
Der Titel muss als kleines Lunova-Vorschaubild klar lesbar sein.
Lieferumfang:
E-Book-Cover (JPG, 2560 x 1600 px), VRL-Print-Umschlag (6 x 9 Zoll, 159 Seiten, Farbdruck)
Das Design darf nicht zu überladen sein.

```html
<!DOCTYPE html>
<html lang="de">
<head>
<meta charset="utf-8">
<title>Der leere Korb – Buchumschlag</title>
<link rel="stylesheet" href="https://fonts.googleapis.com/css2?family=Gelasio:wght@400&family=Cormorant+Garamond:wght@600;700&display=swap">
<style>
  :root {
    --backdrop: #333333;
    --cream: #f1e8da;
    --slate: #8a9da1;
    --slate-text: #8b9ea2;
    --gold: #e2c27a;
    --ink: #1c1c1c;
    --lace-tone: #a9b8bb;
    --shadow-tone: #d9d0c2;
  }
  * { margin: 0; padding: 0; box-sizing: border-box; }
  html, body {
    width: 1200px; height: 675px; overflow: hidden;
    background: var(--backdrop);
  }
  .canvas { position: relative; width: 1200px; height: 675px; }

  .book {
    position: absolute; left: 367px; top: 17px;
    width: 466px; height: 641px;
    background: var(--cream);
  }
  .spine {
    position: absolute; left: 0; top: 0;
    width: 38px; height: 100%;
    background: var(--slate);
  }
  .spine-text {
    position: absolute; left: 19px;
    writing-mode: vertical-rl;
    transform: translateX(-50%);
    color: var(--cream);
    font-family: "Gelasio", serif;
    white-space: nowrap;
  }
  .spine-title { top: 62px; font-size: 29px; line-height: 1; }
  .spine-author { top: 376px; font-size: 17px; line-height: 1; }

  .lace {
    position: absolute; top: 0; height: 100%; width: 40px;
    background: linear-gradient(90deg, var(--lace-tone), #c9d2d2 50%, var(--lace-tone));
  }
  .lace-left { left: 38px; }
  .lace-right { right: 0; }

  .title {
    position: absolute; left: 78px; right: 40px; top: 50px;
    text-align: center;
    font-family: "Gelasio", serif;
    color: var(--slate-text);
    line-height: 1;
  }
  .title-line-1 { display: block; font-size: 46px; letter-spacing: 0.5px; }
  .title-line-2 { display: block; font-size: 66px; margin-top: 6px; }

  .rule {
    position: absolute; left: 135px; width: 234px; height: 1.5px;
    background: var(--gold);
  }
  .rule-top { top: 159px; }
  .rule-mid { top: 429px; }
  .rule-low { top: 522px; }

  .motif {
    position: absolute; left: 131px; top: 184px;
    width: 286px; height: 234px;
    background: radial-gradient(ellipse at 48% 55%, #9a968f 0%, #cfc8bc 55%, var(--cream) 78%);
  }

  .subtitle {
    position: absolute; left: 78px; right: 40px; top: 444px;
    text-align: center;
    font-family: "Gelasio", serif;
    font-size: 13px; line-height: 16px;
    color: var(--ink);
  }

  .bow {
    position: absolute; left: 88px; top: 539px;
    width: 326px; height: 41px;
    background: linear-gradient(180deg, transparent 35%, #3a3a3a 45%, #3a3a3a 55%, transparent 65%);
  }

  .author {
    position: absolute; left: 78px; right: 40px; top: 594px;
    text-align: center;
    font-family: "Cormorant Garamond", serif;
    font-weight: 700;
    font-size: 25px; letter-spacing: 3.5px;
    color: var(--slate-text);
  }
</style>
</head>
<body>
<div class="canvas">
  <div class="book">
    <div class="spine">
      <span class="spine-text spine-title">DER LEERE KORB</span>
      <span class="spine-text spine-author">HELENE MORWITZ</span>
    </div>
    <div class="lace lace-left" role="img" aria-label="Weiße Spitzenborte mit Blumenmuster auf Graublau"></div>
    <div class="lace lace-right" role="img" aria-label="Weiße Spitzenborte mit Blumenmuster auf Graublau"></div>

    <h1 class="title">
      <span class="title-line-1">DER LEERE</span>
      <span class="title-line-2">KORB</span>
    </h1>

    <div class="rule rule-top"></div>
    <div class="motif" role="img" aria-label="Gezeichneter leerer Drahteinkaufskorb mit Schatten"></div>
    <div class="rule rule-mid"></div>

    <p class="subtitle">
      Die No-Buy-Challenge:<br>
      Ein Jahr bewusst nicht kaufen,<br>
      Geld sparen und herausfinden,<br>
      was du wirklich brauchst
    </p>

    <div class="rule rule-low"></div>
    <div class="bow" role="img" aria-label="Schwarze handgezeichnete Schleife mit Band"></div>

    <p class="author">HELENE MORWITZ</p>
  </div>
</div>
</body>
</html>
```